Need Business Cards for my Business

email address: rkpmarlowhollowworks@vendrimail.com
web address: rkpmarlowhollowworks.net
Slogan: We offer various QVN licenses
Rowland K. Pemberly
Please stick with colors of Company Logo
would like the card to be more of the color example of the logo.
If you need PDF copy of logo email me at the above account.
Creative control rests with you.

Industry/Entity Type

Business

Contact Information for Business Card

I am a minimalist, but would like something to pop and stand out amongst other cards, make it memorable.

Font styles to use
Serif
Decorative
Script

```html
<!DOCTYPE html>
<html lang="en">
<head>
<meta charset="utf-8">
<title>Marlow Hollow Works — Business Cards</title>
<link rel="stylesheet" href="https://fonts.googleapis.com/css2?family=Roboto:ital,wght@0,300;0,400;0,700;1,300;1,700&display=swap">
<style>
  :root {
    --backdrop: #e9e5df;
    --card-white: #ffffff;
    --navy: #1f3b66;
    --blue: #1e5aa0;
    --blue-deep: #163f78;
    --red: #d3202f;
    --red-deep: #a8141f;
    --red-bright: #e62a38;
    --ink: #3b3f46;
    --muted: #6b7079;
  }
  * { box-sizing: border-box; margin: 0; padding: 0; }
  html, body { width: 1200px; height: 950px; overflow: hidden; }
  body {
    background: var(--backdrop);
    font-family: "Roboto", Arial, sans-serif;
    display: flex; flex-direction: column; align-items: center; justify-content: center;
    gap: 50px;
  }
  .card {
    position: relative; width: 700px; height: 400px; overflow: hidden;
    box-shadow: 0 10px 28px rgba(0,0,0,.18);
  }
  /* Front */
  .card--front { background: var(--card-white); }
  .front-wave { position: absolute; inset: 0; width: 100%; height: 100%; }
  .brand { position: absolute; left: 48px; bottom: 62px; display: flex; align-items: center; gap: 12px; }
  .brand__dot { width: 18px; height: 18px; border-radius: 50%; background: var(--red); }
  .brand__name { color: var(--navy); font-weight: 700; font-size: 30px; letter-spacing: .5px; }
  .contact { position: absolute; left: 300px; top: 80px; }
  .contact__name { color: var(--navy); font-weight: 700; font-size: 27px; }
  .contact__role { color: var(--red); font-weight: 400; font-size: 17px; margin: 4px 0 18px; }
  .contact__list { list-style: none; }
  .contact__item { display: flex; align-items: center; gap: 10px; color: var(--ink); font-size: 15px; line-height: 27px; }
  .contact__icon { width: 14px; height: 14px; flex: none; fill: var(--navy); }
  /* Back */
  .card--back { background: linear-gradient(135deg, var(--red-bright) 0%, var(--red) 50%, var(--red-deep) 100%); color: #fff; }
  .back-brand { position: absolute; right: 48px; top: 44px; font-weight: 700; font-size: 34px; letter-spacing: .5px; color: #fff; }
  .licenses { position: absolute; left: 56px; top: 140px; list-style: none; }
  .licenses__item { font-weight: 300; font-style: italic; font-size: 17px; line-height: 28px; }
  .slogan { position: absolute; left: 56px; top: 300px; font-weight: 700; font-style: italic; font-size: 19px; }
</style>
</head>
<body>

<section class="card card--front">
  <svg class="front-wave" viewBox="0 0 700 400" preserveAspectRatio="none" aria-hidden="true">
    <path d="M620 0 C560 120 700 260 600 400 L700 400 L700 0 Z" fill="var(--blue)"/>
    <path d="M640 0 C590 140 700 270 630 400 L700 400 L700 0 Z" fill="var(--blue-deep)"/>
    <path d="M596 0 C536 120 676 260 576 400 L588 400 C688 260 548 120 608 0 Z" fill="var(--red)"/>
  </svg>

  <div class="brand">
    <span class="brand__dot"></span>
    <span class="brand__name">Marlow Hollow Works</span>
  </div>

  <div class="contact">
    <h1 class="contact__name">Rowland K. Pemberly</h1>
    <p class="contact__role">CEO/Founder</p>
    <ul class="contact__list">
      <li class="contact__item">
        <svg class="contact__icon" viewBox="0 0 16 16"><path d="M3 1l3 3-2 2c1 2 3 4 5 5l2-2 3 3-2 3C6 14 2 10 1 3z"/></svg>
        301-555-0148
      </li>
      <li class="contact__item">
        <svg class="contact__icon" viewBox="0 0 16 16"><path d="M4 1h8v14H4zM5.5 3v9h5V3z"/></svg>
        836 555 0172
      </li>
      <li class="contact__item">
        <svg class="contact__icon" viewBox="0 0 16 16"><path d="M1 3h14v10H1zM2.5 4.5 8 9l5.5-4.5z"/></svg>
        rkpmarlowhollowworks@vendrimail.com
      </li>
      <li class="contact__item">
        <svg class="contact__icon" viewBox="0 0 16 16"><circle cx="8" cy="8" r="7"/><path d="M1 8h14M8 1c-3 4-3 10 0 14M8 1c3 4 3 10 0 14" stroke="#fff" stroke-width="1" fill="none"/></svg>
        rkpmarlowhollowworks.net
      </li>
    </ul>
  </div>
</section>

<section class="card card--back">
  <div class="back-brand">Marlow Hollow Works</div>
  <ul class="licenses">
    <li class="licenses__item">General Radiotelephone Operator License</li>
    <li class="licenses__item">Marine Radio Operator License Permit</li>
    <li class="licenses__item">Restricted Radio Operators License</li>
    <li class="licenses__item">Radar Maintainers License</li>
    <li class="licenses__item">Radar Endorsement</li>
  </ul>
  <p class="slogan">We offer various QVN licenses</p>
</section>

</body>
</html>
```